Brellow Gateworks garage door installation service and repairs

I need a business card design for my company that is called Brellow Gateworks, I install, service, repair and automate garaged doors.
I want my card to look simple and neat but I also want the information such as contact number, email address and website to be clear and noticeable. I would love a simple logo if possible, I would like to see the color blue in the card but not overpowering.

Industry/Entity Type

Garage

```html
<!DOCTYPE html>
<html lang="en">
<head>
<meta charset="utf-8">
<title>Brellow Gateworks – Business Card</title>
<link rel="stylesheet" href="https://fonts.googleapis.com/css2?family=Oswald:wght@600&family=Roboto+Condensed:wght@400;700&display=swap">
<style>
  :root {
    --backdrop: #3a3a3a;
    --card: #ffffff;
    --ink: #111111;
    --brand-blue: #1a1ae6;
    --faint-tint: #eef0fb;
    --faint-grey: #ececec;
    --rule-grey: #666666;
  }
  html, body {
    margin: 0;
    width: 1200px;
    height: 1000px;
    overflow: hidden;
    background: var(--backdrop);
  }
  .card {
    position: absolute;
    left: 100px;
    top: 215px;
    width: 1000px;
    height: 570px;
    background: var(--card);
    box-shadow: 0 10px 30px rgba(0,0,0,.45);
    overflow: hidden;
    font-family: "Roboto Condensed", "Arial Narrow", sans-serif;
    color: var(--ink);
  }
  .decor-panel {
    position: absolute;
    right: 0;
    top: 90px;
    width: 330px;
    height: 380px;
    background: linear-gradient(180deg, var(--faint-tint), var(--faint-grey));
  }
  .brand {
    position: absolute;
    left: 50px;
    top: 70px;
    width: 470px;
  }
  .brand-row {
    display: flex;
    align-items: center;
    gap: 18px;
  }
  .brand-mark {
    width: 52px;
    height: 52px;
    background: var(--brand-blue);
    flex: none;
  }
  .brand-name {
    font-weight: 700;
    font-size: 54px;
    line-height: 1;
    letter-spacing: 1px;
    text-transform: uppercase;
    color: var(--brand-blue);
  }
  .brand-rule {
    height: 3px;
    background: var(--rule-grey);
    margin: 16px 0 8px;
  }
  .tagline {
    font-size: 15px;
    font-weight: 700;
    letter-spacing: 2.5px;
    text-transform: uppercase;
  }
  .accent-line {
    position: absolute;
    left: 0;
    top: 318px;
    width: 690px;
    height: 8px;
    background: var(--brand-blue);
  }
  .person {
    position: absolute;
    left: 690px;
    top: 232px;
  }
  .person-name {
    font-family: "Oswald", sans-serif;
    font-weight: 600;
    font-variant: small-caps;
    font-size: 40px;
    line-height: 1;
    color: var(--brand-blue);
    margin: 0 0 0 -10px;
  }
  .person-role {
    font-family: "Oswald", sans-serif;
    font-weight: 600;
    font-variant: small-caps;
    font-size: 30px;
    line-height: 1;
    margin: 14px 0 0 80px;
  }
  .contact {
    position: absolute;
    left: 55px;
    top: 360px;
    margin: 0;
    padding: 0;
    list-style: none;
    font-weight: 700;
    font-size: 36px;
    line-height: 50px;
  }
</style>
</head>
<body>
  <main class="card">
    <div class="decor-panel" role="img" aria-label="Faint brand emblem decoration"></div>

    <header class="brand">
      <div class="brand-row">
        <span class="brand-mark"></span>
        <span class="brand-name">Brellow Gateworks</span>
      </div>
      <div class="brand-rule"></div>
      <div class="tagline">Install | Service | Repair and Automate Garaged Doors</div>
    </header>

    <div class="accent-line"></div>

    <section class="person">
      <p class="person-name">Dana Merrit</p>
      <p class="person-role">Owner</p>
    </section>

    <ul class="contact">
      <li>Phone: 555-013-0472</li>
      <li>email@brellowgateworks.com</li>
      <li>www.BrellowGateworks.com</li>
    </ul>
  </main>
</body>
</html>
```